Recruitment Consulting Business Card Design

I require a business card design for my company which is based in Sydney, Australia called Velmora Consulting Group. My company specializes in assisting hotels/resorts across Australia in finding suitable candidates to meet their recruitment needs in the frontline hospitality space. In terms of the candidates I utilise, they are sourced from working holiday visa makers to Australia deriving from Japan, Korea, Taiwan and Hong Kong primarily. The main purpose of the business is to connect both hotels/resorts and individuals together. On one side - hotels/resorts are looking for skilled and willing individuals to work for them, whilst candidates are looking for opportunities to work, make some money, obtain job skills whilst they are living in Australia.

The name of the company Velmora can be looked at as either one word or as two words. It can be abbreviated to Tallow Brook. In essence I view my business as one that connects/brings people and organizations together to mutual benefit.

For my design I would like to see designs that utilze the colors blue, dark blue, silver and white. The logo is the most difficult thing I find to put together as I dont have access to different fonts. You could accentuate on the P in Velmora in designing the logo.

The brand itself should communicate interconnectedness, creativity, innovation and inspiration. I had used those terms Innovate Create Inspire in my original logo which I designed.

Hi there.

I forgot to add in all my details for the card.  The details as follows:

Gareth M Olsen
Director

Suite 8, Level 6
Elm Court, 2-6 Harwick Lane
Chatswood, NSW, 2067
Australia

Mobile: +61 455 727 916
Telephone: +61 2 9736 2045
Email: gareth@velmoraconsulting.com.au

Also, I would like to try designs with a darker navy blue. 

Reason: I have decided to extend the deadline for this project. I thank you all for your designs so far and a few of them are under heavy consideration. Despite the fact that I have provided previous art work for my logo I am looking for someone to put forth an idea for a new logo to be incorporated into the business card. Thank you again for all your hard work and look forward to a further influx of designs. Gareth

Hi All,

QuillHarborStudio is the front runner for the card design. I have attached his image to give you a better idea of where I am at with my decisions.  

Generally speaking we like his design cause it is:

Clean looking 
Modern
Sophisticated, Simple but Professional Looking
Good use of multi colours on the back of the card.

Only thing I am looking to change is to make a new logo and not use the P
I am looking for a circle type logo such as that used by Venthaux in the attachments I have uploaded. Utilizing silver, blue (can try different shades) and silver.

I look forward to more designs and for those that put more effort in at this point I am willing to consider paying extra.

Thank you

Kind Regards,

Gareth

Reason: Extremely busy time at work and I havent had time to review or provide proper feedback. Some great designs out there and decision will be forthcoming at the end of this week.

Target Market(s)

Hotels and Resorts

Industry/Entity Type

Hospitality

Contact Information for Business Card

Gareth M Olsen
Director
Velmora Consulting Group
Suite 8, Level 6, Elm Court, 2-6 Harwick Lane,
Chatswood, NSW, 2067, Australia

Logo Text

Velmora for the main logo with subtext taglines - Create, Innovate, Inspire

Logo styles of interest
Abstract Logo
Wordmark Logo
Requirements
Must have
• A bold but warm design for the word Velmora

Could put the taglines at the bottom - Innovate, Create, Inspire

Keep the business logo clean but sophisticated
Nice to have
• The word Velmora embossed or brought forward and out with silver lines behind the word and logo creating a sense of motion or lines at the left and right of the word Velmora which provides the notion of connecting people/organizations together.

```html
<!DOCTYPE html>
<html lang="en">
<head>
<meta charset="utf-8">
<title>Velmora Consulting – Business Card</title>
<link rel="stylesheet" href="https://fonts.googleapis.com/css2?family=Exo+2:wght@700&family=Source+Sans+3:wght@400;600;700&display=swap">
<style>
  :root {
    --canvas-bg: #ebe8e3;
    --card-bg: #ffffff;
    --brand-blue: #2f6aa3;
    --name-blue: #2d5a86;
    --band-blue: #336799;
    --accent-orange: #f0902a;
    --tagline-blue: #2a6294;
    --contact-text: #3f5873;
    --white: #ffffff;
  }
  * { margin: 0; padding: 0; box-sizing: border-box; }
  html, body {
    width: 1200px; height: 1000px; overflow: hidden;
    background: var(--canvas-bg);
    font-family: "Source Sans 3", "Myriad Pro", sans-serif;
  }
  .canvas { position: relative; width: 1200px; height: 1000px; }

  .card {
    position: absolute;
    width: 739px; height: 415px;
    background: var(--card-bg);
    box-shadow: 0 3px 10px rgba(0,0,0,0.18);
  }
  .card--front { left: 38px; top: 45px; }
  .card--back  { left: 408px; top: 495px; }

  /* Front */
  .front-mark {
    position: absolute; left: 322px; top: 132px;
    width: 80px; height: 80px; border-radius: 50%;
    background: var(--brand-blue);
  }
  .wordmark {
    font-family: "Exo 2", sans-serif; font-weight: 700;
    color: var(--brand-blue); letter-spacing: 1px; line-height: 1;
    position: absolute;
  }
  .wordmark--front { left: 0; width: 739px; text-align: center; top: 226px; font-size: 40px; }
  .division {
    position: absolute; color: var(--accent-orange);
    font-size: 14px; letter-spacing: 1px; line-height: 1;
  }
  .division--front { left: 0; width: 739px; text-align: center; top: 266px; }
  .tagline {
    position: absolute; left: 0; width: 739px; top: 326px;
    display: flex; justify-content: center; align-items: center; gap: 22px;
    color: var(--tagline-blue); font-size: 15px; font-weight: 600;
    letter-spacing: 4px;
  }
  .tagline__divider { width: 1px; height: 20px; background: var(--accent-orange); }

  /* Back */
  .holder { position: absolute; left: 30px; top: 42px; }
  .holder__name { font-size: 25px; font-weight: 700; color: var(--name-blue); line-height: 1; }
  .holder__initial { color: var(--accent-orange); }
  .holder__role {
    margin-top: 4px; font-size: 15px; font-weight: 600;
    color: var(--accent-orange); letter-spacing: 2px;
  }
  .wordmark--back { right: 27px; top: 44px; font-size: 28px; }
  .division--back { right: 49px; top: 72px; font-size: 15px; }
  .address-band {
    position: absolute; left: 0; top: 119px;
    width: 511px; height: 177px; background: var(--band-blue);
    padding: 32px 0 0 31px;
  }
  .address { font-style: normal; color: var(--white); font-size: 20px; line-height: 28px; }
  .back-mark {
    position: absolute; left: 558px; top: 135px;
    width: 130px; height: 130px; border-radius: 50%;
    background: var(--brand-blue);
  }
  .contacts {
    position: absolute; left: 27px; top: 350px;
    display: flex; gap: 22px; align-items: center;
    list-style: none; color: var(--contact-text); font-size: 17px;
  }
  .contact { display: flex; align-items: center; gap: 8px; }
  .contact__icon { width: 20px; height: 20px; flex: none; }
</style>
</head>
<body>
<main class="canvas">

  <section class="card card--front" aria-label="Card front">
    <div class="front-mark" aria-hidden="true"></div>
    <div class="wordmark wordmark--front">VELMORA</div>
    <div class="division division--front">Consulting</div>
    <p class="tagline">
      <span>Innovate</span><span class="tagline__divider"></span>
      <span>Create</span><span class="tagline__divider"></span>
      <span>Inspire</span>
    </p>
  </section>

  <section class="card card--back" aria-label="Card back">
    <div class="holder">
      <h1 class="holder__name"><span class="holder__initial">G</span>areth M Olsen</h1>
      <p class="holder__role">Director</p>
    </div>
    <div class="wordmark wordmark--back">VELMORA</div>
    <div class="division division--back">Consulting</div>

    <div class="address-band">
      <address class="address">
        Suite 8, Level 6<br>
        Elm Court, 2-6 Harwick Lane<br>
        Chatswood, NSW, 2067<br>
        Australia
      </address>
    </div>
    <div class="back-mark" aria-hidden="true"></div>

    <ul class="contacts">
      <li class="contact">
        <svg class="contact__icon" viewBox="0 0 20 20" aria-hidden="true">
          <circle cx="10" cy="10" r="10" fill="var(--accent-orange)"/>
          <rect x="6.5" y="4" width="7" height="12" rx="1.2" fill="none" stroke="#fff" stroke-width="1.5"/>
          <circle cx="10" cy="13.5" r="0.9" fill="#fff"/>
        </svg>
        +61 455 727 916
      </li>
      <li class="contact">
        <svg class="contact__icon" viewBox="0 0 20 20" aria-hidden="true">
          <circle cx="10" cy="10" r="10" fill="var(--accent-orange)"/>
          <path d="M6 5.2c.6-.5 1.4-.4 1.8.2l1 1.6c.3.5.2 1.1-.2 1.5l-.6.6c.6 1.3 1.6 2.3 2.9 2.9l.6-.6c.4-.4 1-.5 1.5-.2l1.6 1c.6.4.7 1.2.2 1.8l-.7.8c-.6.6-1.6.8-2.4.4-2.6-1.2-4.6-3.2-5.8-5.8-.4-.8-.2-1.8.4-2.4z" fill="#fff"/>
        </svg>
        +61 2 9736 2045
      </li>
      <li class="contact">
        <svg class="contact__icon" viewBox="0 0 20 20" aria-hidden="true">
          <circle cx="10" cy="10" r="10" fill="var(--accent-orange)"/>
          <rect x="4.5" y="6.5" width="11" height="7.5" rx="0.8" fill="#fff"/>
          <path d="M4.8 7l5.2 4 5.2-4" fill="none" stroke="var(--accent-orange)" stroke-width="1.2"/>
        </svg>
        gareth@velmoraconsulting.com.au
      </li>
    </ul>
  </section>

</main>
</body>
</html>
```